Business card design

I need my logo on this card, things I need the card to have on it
licensed and insured.
owner operators Derek & Milton Halvorsen
my phone number 5418237906
Disaster Recovery, Storm Damage Restoration, Proactive Disaster Plan Management, Roof Repair/Restoration Structural Repair and Reconstruction, Emergency Boarding and Tarping Service, Perimeter Fencing, Emergency Tree Removal,

```html
<!DOCTYPE html>
<html lang="en">
<head>
<meta charset="utf-8">
<title>Halvorsen's Construction L.L.C — Business Card</title>
<link href="https://fonts.googleapis.com/css2?family=Lato:wght@400;700&display=swap" rel="stylesheet">
<style>
  :root {
    --stage: #e4e1dd;
    --card: #f3f3f2;
    --brand-blue: #1b6fc6;
    --band-blue: #1f78d1;
    --band-blue-dark: #1565c0;
    --stripe-grey: #55585c;
    --text-grey: #3c3f44;
    --white: #ffffff;
  }
  * { margin: 0; padding: 0; box-sizing: border-box; }
  html, body { width: 1200px; height: 900px; overflow: hidden; }
  body {
    background: var(--stage);
    font-family: "Lato", sans-serif;
    position: relative;
  }
  .business-card {
    position: absolute;
    left: 281px; top: 237px;
    width: 670px; height: 383px;
    background: var(--card);
    border-radius: 14px;
    overflow: hidden;
    box-shadow: 0 10px 30px rgba(0,0,0,0.12);
  }
  .card-band { position: absolute; inset: 0; width: 670px; height: 383px; }

  .company-name {
    position: absolute;
    left: 40px; top: 92px; width: 300px;
    display: flex; align-items: center; justify-content: center; gap: 16px;
  }
  .company-mark {
    width: 46px; height: 46px; flex: none;
    background: var(--brand-blue);
  }
  .company-text {
    font-size: 30px; line-height: 36px; font-weight: 400;
    color: var(--brand-blue);
  }

  .contact-block { position: absolute; left: 368px; top: 48px; }
  .owners { font-size: 26px; font-weight: 700; color: var(--brand-blue); letter-spacing: 0.3px; line-height: 30px; }
  .owner-role { font-size: 17px; color: var(--text-grey); margin-top: 1px; margin-left: 2px; line-height: 22px; }
  .contact-list { list-style: none; margin-top: 10px; }
  .contact-list li {
    display: flex; align-items: center; gap: 10px;
    font-size: 15.5px; color: var(--text-grey); height: 23.5px;
  }
  .contact-list svg { width: 13px; height: 13px; fill: var(--brand-blue); flex: none; }
  .credentials { font-size: 20px; font-weight: 700; color: var(--brand-blue); margin-top: 9px; }

  .service-list {
    position: absolute; left: 0; right: 0; top: 291px;
    list-style: none; text-align: center;
    color: var(--white); font-size: 15px; line-height: 19px;
  }
  .service-list li { display: flex; justify-content: center; align-items: center; gap: 5px; white-space: nowrap; }
  .tick { width: 13px; height: 13px; flex: none; }
</style>
</head>
<body>
  <div class="business-card">
    <svg class="card-band" viewBox="0 0 670 383" aria-hidden="true">
      <defs>
        <linearGradient id="bandFill" x1="0" y1="0" x2="1" y2="1">
          <stop offset="0" stop-color="#1f78d1"/>
          <stop offset="1" stop-color="#1565c0"/>
        </linearGradient>
      </defs>
      <polygon points="0,283 336,255 670,281 670,289 336,262 0,290" fill="var(--stripe-grey)"/>
      <polygon points="0,296 336,268 670,294 670,383 0,383" fill="url(#bandFill)"/>
    </svg>

    <div class="company-name">
      <span class="company-mark"></span>
      <span class="company-text">Halvorsen's<br>Construction<br>L.L.C</span>
    </div>

    <div class="contact-block">
      <h1 class="owners">DEREK &amp; MILTON</h1>
      <p class="owner-role">Owner Operators</p>
      <ul class="contact-list">
        <li><svg viewBox="0 0 24 24"><path d="M6.6 10.8c1.4 2.8 3.8 5.1 6.6 6.6l2.2-2.2c.3-.3.7-.4 1-.2 1.1.4 2.3.6 3.6.6.6 0 1 .4 1 1V20c0 .6-.4 1-1 1C10.6 21 3 13.4 3 4c0-.6.4-1 1-1h3.5c.6 0 1 .4 1 1 0 1.3.2 2.5.6 3.6.1.3 0 .7-.2 1z"/></svg>(541) 823-7906</li>
        <li><svg viewBox="0 0 24 24"><path d="M2 5h20v2l-10 6L2 7zm0 4l10 6 10-6v10H2z"/></svg>info@halvorsenbuild.com</li>
        <li><svg viewBox="0 0 24 24"><path d="M12 2a10 10 0 1 0 0 20 10 10 0 0 0 0-20zm-1 17.9A8 8 0 0 1 4.2 10L9 14.8v1a2 2 0 0 0 2 2zm6.9-2.5A2 2 0 0 0 16 16h-1v-3a1 1 0 0 0-1-1H8v-2h2a1 1 0 0 0 1-1V7h2a2 2 0 0 0 2-2v-.4a8 8 0 0 1 2.9 12.8z"/></svg>halvorsenbuild.com</li>
      </ul>
      <p class="credentials">licensed &amp; insured</p>
    </div>

    <ul class="service-list">
      <li>Disaster Recovery <svg class="tick" viewBox="0 0 16 16"><circle cx="8" cy="8" r="8" fill="#fff"/><path d="M4.5 8.2l2.3 2.3 4.7-4.8" stroke="#1f78d1" stroke-width="2" fill="none"/></svg> Storm Damage Restoration</li>
      <li>Proactive Disaster Plan Management <svg class="tick" viewBox="0 0 16 16"><circle cx="8" cy="8" r="8" fill="#fff"/><path d="M4.5 8.2l2.3 2.3 4.7-4.8" stroke="#1f78d1" stroke-width="2" fill="none"/></svg> Roof Repair / Restoration</li>
      <li>Structural Repair &amp; Reconstruction <svg class="tick" viewBox="0 0 16 16"><circle cx="8" cy="8" r="8" fill="#fff"/><path d="M4.5 8.2l2.3 2.3 4.7-4.8" stroke="#1f78d1" stroke-width="2" fill="none"/></svg> Emergency Boarding &amp; Tarping Service</li>
      <li>Perimeter Fencing <svg class="tick" viewBox="0 0 16 16"><circle cx="8" cy="8" r="8" fill="#fff"/><path d="M4.5 8.2l2.3 2.3 4.7-4.8" stroke="#1f78d1" stroke-width="2" fill="none"/></svg> Emergency Tree Removal</li>
    </ul>
  </div>
</body>
</html>
```